Business Card Design

I am a Special Event Consultant,I arrange and organise Special Events - Product Launches,Sponsorship and Product Displays.

I would like the RTV to be a feature of the design with 'Special Event Services" underneath - keep it very simple but creative using this information. So it is just the letters "RTV" with Event Services underneath.

(Simple Colours - Silver, Black, Grey - no bright colours - We work for Valtoria Drenn,KDX, Lyndrel So it is class and classic.)

Only my Name and mobile on the front.

Contact Information for Business Card

FRONT
Tess Varnholt
Tel: 0436 218907

BACK
Email: tess@rtveventservices.example.au

2807 Wexbury Heights,83 Pollard Street
NORTHVALE.Vic.3158.

```html
<!DOCTYPE html>
<html lang="en">
<head>
<meta charset="UTF-8">
<title>RTV Special Event Services – Business Card</title>
<link rel="stylesheet" href="https://fonts.googleapis.com/css2?family=Cinzel:wght@400&family=Raleway:wght@300;400&display=swap">
<style>
  :root {
    --stage: #ecebe9;
    --card-edge: #ffffff;
    --front-ink: #0b0b0b;
    --silver: #c9c9c9;
    --silver-soft: #a9a9a9;
    --back-paper: #e4e4e4;
    --back-rule: #bdbdbd;
    --back-text: #1d1d1d;
  }
  html, body {
    margin: 0;
    padding: 0;
    width: 1200px;
    height: 757px;
    overflow: hidden;
    background: var(--stage);
  }
  .canvas {
    position: relative;
    width: 1200px;
    height: 757px;
    display: flex;
    align-items: center;
    justify-content: center;
    gap: 60px;
  }
  .card {
    position: relative;
    width: 500px;
    height: 286px;
    background: var(--card-edge);
    box-shadow: 0 6px 18px rgba(0,0,0,0.18);
    box-sizing: border-box;
    padding: 12px;
  }
  .card__panel {
    position: relative;
    width: 100%;
    height: 100%;
    box-sizing: border-box;
  }
  .card__frame {
    position: absolute;
    inset: 7px;
    border: 1px solid;
  }

  /* Front */
  .card--front .card__panel { background: var(--front-ink); }
  .card--front .card__frame { border-color: var(--silver-soft); }
  .front-content {
    position: absolute;
    inset: 0;
    display: flex;
    flex-direction: column;
    align-items: center;
    justify-content: center;
    color: var(--silver);
    text-align: center;
  }
  .brand-mark {
    font-family: 'Cinzel', serif;
    font-size: 30px;
    letter-spacing: 14px;
    margin-right: -14px;
    line-height: 1;
  }
  .brand-tagline {
    font-family: 'Raleway', sans-serif;
    font-weight: 300;
    font-size: 17px;
    letter-spacing: 0.5px;
    margin-top: 6px;
  }
  .flourish {
    width: 66px;
    height: 22px;
    margin: 6px 0 4px;
    border-radius: 11px;
    background: linear-gradient(90deg, rgba(201,201,201,0.15), rgba(201,201,201,0.45), rgba(201,201,201,0.15));
  }
  .holder-name {
    font-family: 'Raleway', sans-serif;
    font-weight: 400;
    font-size: 25px;
    letter-spacing: 0.5px;
  }
  .holder-phone {
    font-family: 'Raleway', sans-serif;
    font-weight: 300;
    font-size: 18px;
    margin-top: 4px;
  }

  /* Back */
  .card--back .card__panel { background: var(--back-paper); }
  .card--back .card__frame { border-color: var(--back-rule); }
  .back-content {
    position: absolute;
    left: 44px;
    right: 20px;
    bottom: 44px;
    font-family: 'Raleway', sans-serif;
    color: var(--back-text);
    font-size: 17px;
    line-height: 1.45;
  }
  .contact-email .label { font-size: 14px; margin-right: 6px; }
  .contact-address { margin: 0; font-style: normal; }
  .contact-address .locality { display: block; padding-left: 66px; }
</style>
</head>
<body>
  <main class="canvas">
    <section class="card card--front" aria-label="Business card front">
      <div class="card__panel">
        <div class="card__frame"></div>
        <div class="front-content">
          <div class="brand-mark">RTV</div>
          <div class="brand-tagline">Special Event Services</div>
          <div class="flourish" role="img" aria-label="Decorative silver scroll flourish"></div>
          <div class="holder-name">Tess Varnholt</div>
          <div class="holder-phone">Tel: 0436 218907</div>
        </div>
      </div>
    </section>

    <section class="card card--back" aria-label="Business card back">
      <div class="card__panel">
        <div class="card__frame"></div>
        <div class="back-content">
          <div class="contact-email"><span class="label">Email:</span>tess@rtveventservices.example.au</div>
          <address class="contact-address">
            2807 Wexbury Heights,83 Pollard Street
            <span class="locality">NORTHVALE.Vic.3158.</span>
          </address>
        </div>
      </div>
    </section>
  </main>
</body>
</html>
```